Sharper Daily Habits Qorafone App

I am looking to create an Qorafone app (support Qorafone 5 and above) that will inspire and empower the app user to be more productive through a creative, interative and simplistic user experience that teaches the 10 topics related to "Sharper Daily Habits". Please see attached zip files for the 10 topic as PDF files and 20 posters (20 jpg files) which include a quote related to the content bundle’s topic.

Target Market(s)

working professionals who desire to be more productive in their ways of doing

Industry/Entity Type

It Support

Font styles to use
Sans Serif

Colors
33a6d7
0255a3
9bcb3b
cadf82
33b8a4

Requirements
Must have
• don't really wanna say "ebook" style app which would be below my expectation, i expect something more creative than an "ebook" app. i prefer you use your creativity to come up with the design but if you are a bit lost, please read below.
• some specs in my mind:
• - 10 flash cards design for each of the topic so they can be used in a carousel style menu (see sample app screenshot 1 - 1st screen to the left)
• - when presenting a topic, the background should be the same as the flash card of the topic (see sample app screenshot 2 - the right most screen)
• - at the bottom of the topic screen, a audio play/pause buttons bar should be presented as the app will play audible version for the article.
• - the fashion of the sample app screen shots shouldn't be followed as it is an ancient fashion reflecting the content. I expect the fashion of the app should be modern and reflect the topic "sharper daily habits"
• Screens required:
• - Main menu screen: carosoul style presenting the 10 topics using flash cards, should have a "play/pause" button to play the audible topic
• - Topic screen: presents the text content of the topic with flash card design as the background, paging buttons when content spans over one page, have media player bar at bottom to "play/pause/fast forward/reverse" audible
Nice to have
• i have 20 posters with quotes that inspires the user. i would like to see the posters to be presented full screen with a "inspire me" button somewhere which will randomly display a poster to the user.

```html
<!DOCTYPE html>
<html lang="en">
<head>
<meta charset="utf-8">
<title>Sharper Daily Habits – Topic 3</title>
<link rel="stylesheet" href="https://fonts.googleapis.com/css2?family=Montserrat:wght@300;400;600&display=swap">
<style>
  :root {
    --bg: #ffffff;
    --brand-navy: #0255a3;
    --brand-sky: #33a6d7;
    --brand-teal: #33b8a4;
    --brand-lime: #9bcb3b;
    --brand-pale: #cadf82;
    --ink: #3b4a5a;
    --ink-muted: #6f7e8c;
    --body-grey: #a3a3a3;
    --poster-teal: #5ec8b4;
    --poster-orange: #e8763a;
    --poster-cream: #efe4c8;
    --poster-dark: #3a2a22;
  }
  * { margin: 0; padding: 0; box-sizing: border-box; }
  html, body { width: 712px; height: 1200px; overflow: hidden; background: var(--bg); }
  body { position: relative; font-family: "Montserrat", Arial, sans-serif; color: var(--ink); }

  .status-bar {
    position: absolute; top: 12px; left: 22px; right: 22px; height: 26px;
    display: flex; align-items: center; justify-content: space-between;
    font-size: 19px; font-weight: 400; color: var(--ink);
  }
  .status-left, .status-right { display: flex; align-items: center; gap: 6px; width: 210px; }
  .status-right { justify-content: flex-end; }
  .signal { display: flex; gap: 3px; }
  .signal span { width: 9px; height: 9px; border-radius: 50%; border: 1.5px solid var(--ink); }
  .signal span.on { background: var(--ink); }
  .battery { width: 42px; height: 16px; border: 1.5px solid var(--ink); border-radius: 3px; padding: 2px; position: relative; }
  .battery::after { content: ""; position: absolute; right: -5px; top: 4px; width: 3px; height: 6px; background: var(--ink); border-radius: 0 2px 2px 0; }
  .battery-fill { width: 100%; height: 100%; background: var(--ink-muted); border-radius: 1px; }

  .nav-bar {
    position: absolute; top: 62px; left: 38px; right: 46px; height: 40px;
    display: flex; align-items: center; justify-content: space-between;
    font-size: 24px; font-weight: 400; color: var(--ink);
  }
  .nav-back { display: flex; align-items: center; gap: 10px; width: 150px; }
  .nav-counter { font-weight: 600; font-size: 26px; color: var(--brand-navy); }
  .nav-share { width: 150px; text-align: right; color: var(--ink-muted); }

  .poster-thumb {
    position: absolute; top: 150px; left: 261px; width: 190px; height: 190px; border-radius: 50%;
    background: linear-gradient(180deg, var(--poster-teal) 0%, var(--poster-teal) 30%, var(--poster-orange) 30%, var(--poster-orange) 42%, var(--poster-cream) 42%, var(--poster-cream) 72%, var(--poster-dark) 72%);
  }

  .topic-title {
    position: absolute; top: 420px; left: 0; right: 0; text-align: center;
    font-weight: 600; font-size: 29px; letter-spacing: -0.4px;
    color: var(--brand-navy);
  }

  .topic-text {
    position: absolute; left: 108px; right: 108px; text-align: center;
    font-weight: 300; font-size: 19.5px; line-height: 29px; color: var(--body-grey);
  }
  .para-1 { top: 530px; }
  .para-2 { top: 722px; }
  .para-3 { top: 898px; }

  .media-bar {
    position: absolute; top: 1052px; left: 176px; width: 360px; height: 62px; border-radius: 31px;
    background: linear-gradient(90deg, var(--brand-sky), var(--brand-teal));
    display: flex; align-items: center; justify-content: space-between; padding: 0 18px;
    color: #fff; box-shadow: 0 3px 8px rgba(2, 85, 163, 0.25);
  }
  .media-play { display: flex; align-items: center; gap: 12px; font-weight: 600; font-size: 16px; letter-spacing: 0.2px; }
  .media-skip { display: flex; align-items: center; }
</style>
</head>
<body>
  <header class="status-bar">
    <div class="status-left">
      <div class="signal"><span class="on"></span><span class="on"></span><span class="on"></span><span></span><span></span></div>
      <span>NOVA</span>
      <svg width="20" height="16" viewBox="0 0 20 16" aria-hidden="true">
        <path d="M2 6a11 11 0 0 1 16 0M5 9a7 7 0 0 1 10 0M8 12a3 3 0 0 1 4 0" fill="none" stroke="#3b4a5a" stroke-width="2" stroke-linecap="round"/>
        <circle cx="10" cy="14.5" r="1.3" fill="#3b4a5a"/>
      </svg>
    </div>
    <span class="status-time">4:21 PM</span>
    <div class="status-right">
      <svg width="12" height="20" viewBox="0 0 12 20" aria-hidden="true">
        <path d="M1 5l9 9-4.5 4V2L10 6 1 15" fill="none" stroke="#6f7e8c" stroke-width="1.6" stroke-linejoin="round"/>
      </svg>
      <span>100%</span>
      <div class="battery"><div class="battery-fill"></div></div>
    </div>
  </header>

  <nav class="nav-bar">
    <div class="nav-back">
      <svg width="14" height="24" viewBox="0 0 14 24" aria-hidden="true">
        <path d="M12 2L3 12l9 10" fill="none" stroke="#3b4a5a" stroke-width="3" stroke-linecap="round" stroke-linejoin="round"/>
      </svg>
      <span>Back</span>
    </div>
    <div class="nav-counter">3/20</div>
    <div class="nav-share">Share</div>
  </nav>

  <div class="poster-thumb" role="img" aria-label="Round thumbnail of a retro quote poster about productivity"></div>

  <h1 class="topic-title">PRODUCTIVITY IS HAPPINESS</h1>

  <p class="topic-text para-1">Whenever you finish an activity, clean up to reduce the friction to starting it the next time. E.g. clean the kitchen when you finish cooking, or set aside your running gear for your run to-morrow morning.</p>
  <p class="topic-text para-2">We all waste an inordinate amount of time checking and responding to email. I've got a bad habit of wasting more time than I should ensuring my emails come across as well worded and polite.</p>
  <p class="topic-text para-3">If everyone knows that we are responding with brief, straight to the point answers, then (with any luck) no one will take it personally.</p>

  <div class="media-bar" role="group" aria-label="Audio player">
    <span class="media-skip" aria-label="Rewind">
      <svg width="30" height="20" viewBox="0 0 30 20" aria-hidden="true">
        <path d="M14 3L3 10l11 7zM27 3L16 10l11 7z" fill="#fff"/>
      </svg>
    </span>
    <span class="media-play">
      <svg width="42" height="42" viewBox="0 0 44 44" aria-hidden="true">
        <circle cx="22" cy="22" r="20" fill="none" stroke="#fff" stroke-width="1.8"/>
        <path d="M18 14l11 8-11 8z" fill="none" stroke="#fff" stroke-width="1.8" stroke-linejoin="round"/>
      </svg>
      <span>PLAY AS AUDIO</span>
    </span>
    <span class="media-skip" aria-label="Fast forward">
      <svg width="30" height="20" viewBox="0 0 30 20" aria-hidden="true">
        <path d="M3 3l11 7-11 7zM16 3l11 7-11 7z" fill="#fff"/>
      </svg>
    </span>
  </div>
</body>
</html>
```